Software company specialized in data analytics and professional services

We need a landing page design for our business. It should include our logo design. It should have multiple sections :
- stylish head
- what we do (data analytics software, professional services)
- contact form

Target Market(s)

Companies, B2B

Industry/Entity Type

Data

Number of Pages Required

1 page

Font styles to use
Sans Serif

Requirements
Must have
• Dark theme
Should not have
• Gradients on buttons

```html
<!DOCTYPE html>
<html lang="en">
<head>
<meta charset="utf-8">
<title>VANTAGRID — Data Analytics Software &amp; Services</title>
<link rel="stylesheet" href="https://fonts.googleapis.com/css2?family=Poppins:wght@300;400;500;600;700&display=swap">
<style>
:root{
  --ink:#0b0b12;
  --navy:#14163a;
  --hero-dark:#1c2233;
  --magenta:#b412b8;
  --purple:#6a1fb0;
  --deep-blue:#1d2a6b;
  --teal:#0e4f7a;
  --paper:#ffffff;
  --mist:#f3f3f4;
  --text:#4a4a55;
  --muted:#6b6b76;
  --night:#0c0f12;
  --field:#ffffff;
}
*{margin:0;padding:0;box-sizing:border-box}
html,body{width:1200px;height:2956px;overflow:hidden}
body{font-family:"Poppins",sans-serif;color:var(--text);background:var(--paper);position:relative}
.abs{position:absolute}

/* header */
.site-header{left:0;top:0;width:1200px;height:81px;background:var(--paper);z-index:3}
.brand{left:134px;top:24px;font-weight:600;font-size:30px;letter-spacing:0.5px;color:var(--magenta)}
.btn{display:inline-flex;align-items:center;justify-content:center;border-radius:24px;background:var(--purple);color:#fff;font-weight:600;font-size:14px;letter-spacing:0.6px;text-decoration:none}
.header-cta{left:946px;top:22px;width:134px;height:44px}

/* hero */
.hero{left:0;top:81px;width:1200px;height:600px;background:var(--hero-dark);clip-path:polygon(0 0,100% 0,100% 81.5%,0 100%)}
.hero-visual{left:440px;top:0;width:760px;height:600px;background:radial-gradient(ellipse at 60% 35%,rgba(90,60,200,.55),transparent 60%),linear-gradient(160deg,#2a3352 0%,#1e2740 55%,#3a3a4a 100%)}
.hero-shade{left:0;top:0;width:700px;height:600px;background:linear-gradient(90deg,var(--hero-dark) 55%,transparent)}
.social-rail{left:80px;top:240px;width:20px}
.social-rail span{display:block;width:18px;height:18px;border-radius:50%;border:2px solid #c9cbd4;margin-bottom:20px}
.rail-line{left:89px;top:445px;width:2px;height:80px;background:#d8d8de}
.rail-label{left:60px;top:580px;transform:rotate(-90deg);color:#fff;font-size:13px;letter-spacing:4px;font-weight:500}
.hero-title{left:190px;top:232px;color:#fff;font-size:43px;line-height:51px;letter-spacing:1.5px;font-weight:400}
.hero-title strong{font-weight:600}
.hero-lede{left:190px;top:400px;color:#fff;font-size:14px;line-height:22px}
.hero-cta{left:190px;top:484px;width:138px;height:43px}
.corner-shard{left:944px;top:570px;width:256px;height:156px;background:#efeff1;clip-path:polygon(0 20%,100% 0,0 100%)}

/* about */
.about-visual{left:175px;top:752px;width:375px;height:476px;border-radius:120px;background:linear-gradient(180deg,#2b2a6e 0%,#5a5a66 30%,#b61ad0 42%,#8a8a92 55%,#1f6a8a 85%,#231d5e 100%)}
.about-title{left:622px;top:842px;font-size:37px;color:var(--ink);font-weight:400;letter-spacing:1px}
.about-title strong{font-weight:600}
.about-copy{left:622px;top:920px;width:405px;font-size:13.6px;line-height:22px;color:var(--text)}
.about-copy p{margin-bottom:21px}
.about-copy b{color:#222;font-weight:600}
.values{left:622px;top:1155px;display:flex;gap:18px;font-size:13.5px;font-weight:600;color:var(--deep-blue)}
.values span{display:flex;align-items:center;gap:5px}

/* services */
.services{left:0;top:1215px;width:1200px;height:1030px;background:var(--mist);clip-path:polygon(0 12%,100% 0,100% 100%,0 100%)}
.left-shard{left:71px;top:1207px;width:175px;height:213px;background:#fff;clip-path:polygon(0 0,100% 45%,0 100%)}
.services-title{left:0;top:1390px;width:1200px;text-align:center;font-size:37px;color:var(--ink);letter-spacing:1px}
.services-title strong{font-weight:600}
.services-lede{left:340px;top:1460px;width:520px;text-align:center;font-size:13.6px;line-height:22px}
.services-lede b{font-weight:600;color:#333}
.hub{left:0;top:1540px;width:1200px;height:170px}
.card{top:1730px;width:273px;text-align:center}
.card h3{font-size:15.5px;line-height:21px;font-weight:600;color:#2b2b33;margin-top:18px}
.card p{font-size:13.6px;line-height:22px;color:var(--muted);margin-top:20px}
.card a{display:inline-block;margin-top:22px;font-size:13.5px;font-weight:600;color:var(--magenta);text-decoration:none}
.card-base{top:2024px;width:273px;height:18px;border:3px solid var(--teal);border-top:none;border-radius:0 0 14px 14px}
.card-base.is-active{border-color:var(--magenta)}

/* contact */
.contact{left:0;top:2133px;width:1200px;height:823px;background:var(--night);clip-path:polygon(0 13.6%,100% 0,100% 100%,0 100%)}
.contact-visual{left:0;top:2133px;width:1200px;height:700px;background:radial-gradient(ellipse at 58% 45%,rgba(40,120,70,.35),transparent 55%),radial-gradient(ellipse at 30% 70%,rgba(30,90,80,.25),transparent 50%);clip-path:polygon(0 16%,100% 0,100% 100%,0 100%)}
.contact-title{left:162px;top:2320px;font-size:37px;color:#fff;letter-spacing:1.5px}
.contact-title strong{font-weight:600}
.contact-rule{left:166px;top:2382px;width:141px;height:3px;background:#fff}
.info{left:162px;display:flex;gap:24px;color:#fff}
.info .dot{width:56px;height:56px;border-radius:50%;background:var(--magenta);display:flex;align-items:center;justify-content:center;flex:none}
.info h4{font-size:15.5px;font-weight:600;margin-top:2px}
.info p{font-size:13.6px;line-height:18px;color:#e4e4ea;margin-top:3px}
.field{background:var(--field);clip-path:polygon(0 0,100% 0,100% 70%,94% 100%,0 100%);display:flex;align-items:flex-start;padding:27px 0 0 24px;font-size:13.6px;color:#666;gap:6px}
.field.msg{clip-path:polygon(0 0,100% 0,100% 88%,97% 100%,0 100%)}
.submit{left:510px;top:2691px;width:136px;height:43px}
.footer-rule{left:170px;top:2843px;width:861px;height:1px;background:#3a3d44}
.footer-social{left:163px;top:2875px;display:flex;gap:19px}
.footer-social span{width:18px;height:18px;border-radius:50%;border:2px solid #c9cbd4}
.copyright{left:700px;top:2873px;width:327px;text-align:right;color:#fff;font-size:14.5px}
.copyright b{font-weight:600}
</style>
</head>
<body>

<header class="site-header abs">
  <div class="brand abs">VANTAGRID</div>
  <a class="btn header-cta abs" href="#contact">Contact Us</a>
</header>

<section class="hero abs">
  <div class="hero-visual abs" role="img" aria-label="Hands at a keyboard beneath floating holographic analytics dashboards with bar charts, a world map and a donut chart"></div>
  <div class="hero-shade abs"></div>
</section>
<div class="social-rail abs"><span></span><span></span><span></span><span></span><span></span></div>
<div class="rail-line abs"></div>
<div class="rail-label abs">CONNECT</div>
<h1 class="hero-title abs">Pioneering<br><strong>Precision In Data<br>Excellence</strong></h1>
<p class="hero-lede abs">transformative analytics software and expert services<br>redefining your data strategy</p>
<a class="btn hero-cta abs" href="#services">Get Started</a>
<div class="corner-shard abs"></div>

<section class="about">
  <div class="about-visual abs" role="img" aria-label="Black and white photo of a person reviewing financial statistics on a tablet, framed in a rounded shape with blue and magenta bands"></div>
  <h2 class="about-title abs">About <strong>VANTAGRID</strong></h2>
  <div class="about-copy abs">
    <p>At <b>VANTAGRID</b>, we stand at the forefront of innovation, pioneering precision in data excellence. <b>Our mission is</b> to empower businesses with transformative analytics software and expert services, elevating data strategies to new heights.</p>
    <p>With a commitment to unlocking insights and unleashing potential, VANTAGRID is your dedicated partner on the journey to data-driven success.</p>
  </div>
  <div class="values abs">
    <span><svg width="14" height="12" viewBox="0 0 14 12"><path d="M1 6l4 4 8-9" fill="none" stroke="currentColor" stroke-width="1.8"/></svg>Precision</span>
    <span><svg width="14" height="12" viewBox="0 0 14 12"><path d="M1 6l4 4 8-9" fill="none" stroke="currentColor" stroke-width="1.8"/></svg>Innovation</span>
    <span><svg width="14" height="12" viewBox="0 0 14 12"><path d="M1 6l4 4 8-9" fill="none" stroke="currentColor" stroke-width="1.8"/></svg>Partnership</span>
  </div>
</section>

<section class="services abs" id="services"></section>
<div class="left-shard abs"></div>
<h2 class="services-title abs"><strong>What We</strong> Do</h2>
<p class="services-lede abs">At <b>VANTAGRID</b>, we redefine the landscape of data analytics, blending cutting-edge software solutions with unparalleled professional services.</p>
<svg class="hub abs" viewBox="0 0 1200 170">
  <circle cx="600" cy="42" r="39" fill="none" stroke="#c7c7cc" stroke-dasharray="6 6"/>
  <circle cx="600" cy="42" r="13" fill="none" stroke="#6a1fb0" stroke-width="4"/>
  <circle cx="575" cy="105" r="4" fill="#555"/><circle cx="600" cy="120" r="4" fill="#555"/><circle cx="623" cy="105" r="4" fill="#555"/>
  <path d="M575 110v20q0 6-6 6H302q-6 0-6 6v26M600 125v45M623 110v20q0 6 6 6h267q6 0 6 6v26" fill="none" stroke="#999" stroke-dasharray="3 3"/>
</svg>

<article class="card abs" style="left:159px">
  <svg width="72" height="46" viewBox="0 0 72 46"><path d="M8 2H2v42h6M64 2h6v42h-6" fill="none" stroke="#1d2a6b" stroke-width="4"/><circle cx="36" cy="21" r="11" fill="none" stroke="#b412b8" stroke-width="1.8"/><path d="M26 38h20" stroke="#1d2a6b" stroke-width="1.8"/></svg>
  <h3>Predictive Analytics<br>Solutions</h3>
  <p>Harness the power of advanced algorithms and historical data to forecast trends, identify opportunities, and mitigate risks.</p>
  <a href="#contact">Get Started &rarr;</a>
</article>
<article class="card abs" style="left:463px">
  <svg width="72" height="46" viewBox="0 0 72 46"><path d="M8 2H2v42h6M64 2h6v42h-6" fill="none" stroke="#1d2a6b" stroke-width="4"/><rect x="22" y="10" width="12" height="10" fill="none" stroke="#b412b8" stroke-width="1.8"/><rect x="38" y="10" width="12" height="10" fill="none" stroke="#1d2a6b" stroke-width="1.8"/><circle cx="36" cy="32" r="6" fill="none" stroke="#b412b8" stroke-width="1.8"/></svg>
  <h3>Custom Data<br>Strategy Consulting</h3>
  <p>From data governance to implementation roadmaps, we guide you on a transformative journey to data excellence.</p>
  <a href="#contact">Get Started &rarr;</a>
</article>
<article class="card abs" style="left:765px">
  <svg width="72" height="46" viewBox="0 0 72 46"><path d="M8 2H2v42h6M64 2h6v42h-6" fill="none" stroke="#1d2a6b" stroke-width="4"/><rect x="20" y="10" width="32" height="24" fill="none" stroke="#1d2a6b" stroke-width="1.8"/><path d="M24 28l7-7 5 4 10-9" fill="none" stroke="#b412b8" stroke-width="1.8"/></svg>
  <h3>Real-time Reporting<br>and Dashboards</h3>
  <p>Experience the power of instantaneous insights that translate complex data into actionable information.</p>
  <a href="#contact">Get Started &rarr;</a>
</article>
<div class="card-base abs" style="left:162px"></div>
<div class="card-base abs is-active" style="left:463px"></div>
<div class="card-base abs" style="left:757px"></div>

<section class="contact abs" id="contact"></section>
<div class="contact-visual abs" role="img" aria-label="Dark futuristic technology backdrop with faint green circular interface rings and circuit lines"></div>
<h2 class="contact-title abs">Contact <strong>Us</strong></h2>
<div class="contact-rule abs"></div>

<div class="info abs" style="top:2434px">
  <div class="dot"><svg width="20" height="24" viewBox="0 0 20 24"><path d="M10 1a8 8 0 0 0-8 8c0 6 8 14 8 14s8-8 8-14a8 8 0 0 0-8-8z" fill="#fff"/><circle cx="10" cy="9" r="3" fill="#b412b8"/></svg></div>
  <div><h4>Location</h4><p>2740 Larchmont Ave.<br>Brookvale, Oregon 97403</p></div>
</div>
<div class="info abs" style="top:2528px">
  <div class="dot"><svg width="20" height="20" viewBox="0 0 24 24"><path d="M6.6 10.8a15 15 0 0 0 6.6 6.6l2.2-2.2a1 1 0 0 1 1-.25 11 11 0 0 0 3.6.6 1 1 0 0 1 1 1V20a1 1 0 0 1-1 1A17 17 0 0 1 3 4a1 1 0 0 1 1-1h3.5a1 1 0 0 1 1 1c0 1.25.2 2.45.6 3.6a1 1 0 0 1-.25 1z" fill="#fff"/></svg></div>
  <div><h4>Phone</h4><p>(503) 555-0172</p></div>
</div>
<div class="info abs" style="top:2618px">
  <div class="dot"><svg width="22" height="16" viewBox="0 0 22 16"><rect width="22" height="16" rx="2" fill="#fff"/><path d="M1 2l10 7 10-7" fill="none" stroke="#b412b8" stroke-width="1.8"/></svg></div>
  <div><h4>Email</h4><p>dana.wells@example.com</p></div>
</div>

<form class="contact-form">
  <div class="field abs" style="left:510px;top:2350px;width:252px;height:60px">&#9711; Name</div>
  <div class="field abs" style="left:779px;top:2350px;width:252px;height:60px">&#9906; Company</div>
  <div class="field abs" style="left:510px;top:2434px;width:252px;height:60px">&#9993; Email</div>
  <div class="field abs" style="left:779px;top:2434px;width:252px;height:60px">&#9743; Phone</div>
  <div class="field msg abs" style="left:510px;top:2521px;width:521px;height:134px">&#9633; Message</div>
  <a class="btn submit abs" href="#contact">Get Started</a>
</form>

<div class="footer-rule abs"></div>
<div class="footer-social abs"><span></span><span></span><span></span><span></span><span></span></div>
<p class="copyright abs">© 2023 All Rights Reserved | <b>VANTAGRID</b></p>

</body>
</html>
```